Hotel Company Personal Business Card

This is a hotel business, personal business card. Need it sleek, professional, and sharp looking. I have a design attached that we can work with. My turnaround time is April 8th. I would need the cards by then. One side only color, the other side all details. This is flexible depending on the designs you come up with. I would like a boutique, unique, modern type of touch to the business card. Memorable type of card that people will want to keep.

Target Market(s)

Business professionals

Industry/Entity Type

Hospitality/Hotels & Resorts

Contact Information for Business Card

Name, email, phone number, address, and ASHFORD HOUSE. Anything unique

Font styles to use
Serif
Sans Serif

Colors

Designer to choose colors to be used in the design.

Requirements
Nice to have
• Neutral colors. Eye popping logo. Sleek design. Boutique feel. Hint of color.

```html
<!DOCTYPE html>
<html lang="en">
<head>
<meta charset="utf-8">
<title>Ashford House — Business Card</title>
<link href="https://fonts.googleapis.com/css2?family=Lato:ital,wght@0,400;0,700;1,400&family=Montserrat:wght@500;600;800&display=swap" rel="stylesheet">
<style>
  :root {
    --backdrop: #25272b;
    --navy: #15364f;
    --navy-deep: #0f2b40;
    --gold: #d4b083;
    --gold-soft: #e7d3b6;
    --paper: #ffffff;
    --ink: #0f3350;
    --grey: #6b6f74;
  }
  * { margin: 0; padding: 0; box-sizing: border-box; }
  html, body { width: 1200px; height: 952px; overflow: hidden; }
  body {
    background: var(--backdrop);
    display: flex; flex-direction: column; align-items: center; justify-content: center;
    gap: 60px;
    font-family: "Lato", sans-serif;
  }
  .card {
    position: relative;
    width: 700px; height: 400px;
    overflow: hidden;
    box-shadow: 0 14px 30px rgba(0,0,0,.45);
  }

  /* Front: navy side */
  .card--front { background: var(--navy); }
  .pattern-band {
    position: absolute; top: 0; bottom: 0; width: 92px;
  }
  .card--front .pattern-band {
    background: linear-gradient(135deg, var(--navy-deep), #2a4456 50%, var(--navy-deep));
  }
  .card--front .pattern-band--left { left: 0; }
  .card--front .pattern-band--right { right: 0; }
  .dot-rule {
    position: absolute; top: 14px; bottom: 14px; width: 4px;
    background-image: radial-gradient(circle, var(--gold) 1.6px, transparent 2px);
    background-size: 4px 20px;
    background-repeat: repeat-y;
  }
  .card--front .dot-rule--left { left: 112px; }
  .card--front .dot-rule--right { right: 112px; }
  .front-content {
    position: absolute; inset: 0;
    display: flex; flex-direction: column; align-items: center; justify-content: center;
    color: var(--gold);
  }
  .front-url { font-size: 15px; letter-spacing: .5px; margin-bottom: 34px; }
  .brand-square {
    width: 96px; height: 96px;
    border: 2px solid var(--gold); border-radius: 14px;
    margin-bottom: 30px;
  }
  .brand-name {
    font-family: "Montserrat", sans-serif; font-weight: 500;
    font-size: 28px; letter-spacing: 3px;
  }

  /* Back: white details side */
  .card--back { background: var(--paper); }
  .card--back .pattern-band {
    right: 0; width: 230px;
    background: linear-gradient(135deg, #f3e7d6, var(--gold-soft) 50%, #f6ede1);
  }
  .card--back .dot-rule { right: 252px; }
  .person { position: absolute; left: 64px; top: 52px; }
  .person-name {
    font-family: "Montserrat", sans-serif; font-size: 27px;
    color: var(--ink); letter-spacing: 1px; font-weight: 500;
  }
  .person-name strong { font-weight: 800; }
  .person-role { font-size: 15px; color: var(--grey); margin-top: 2px; }
  .person-rule { width: 62px; height: 2px; background: #8a8d90; margin-top: 10px; }
  .contacts {
    position: absolute; left: 64px; top: 178px;
    list-style: none; font-size: 15px; color: var(--grey);
  }
  .contacts li { display: flex; align-items: flex-start; gap: 12px; margin-bottom: 10px; line-height: 1.3; }
  .contact-icon {
    flex: none; width: 20px; height: 20px; border-radius: 3px;
    background: var(--ink); display: flex; align-items: center; justify-content: center;
  }
  .contact-icon svg { width: 13px; height: 13px; }
</style>
</head>
<body>

  <section class="card card--front" aria-label="Card front">
    <div class="pattern-band pattern-band--left" role="img" aria-label="Gold geometric lattice pattern on navy"></div>
    <div class="pattern-band pattern-band--right" role="img" aria-label="Gold geometric lattice pattern on navy"></div>
    <div class="dot-rule dot-rule--left"></div>
    <div class="dot-rule dot-rule--right"></div>
    <div class="front-content">
      <p class="front-url">www.ashfordstay.com</p>
      <div class="brand-square"></div>
      <h1 class="brand-name">ASHFORD HOUSE</h1>
    </div>
  </section>

  <section class="card card--back" aria-label="Card back">
    <div class="person">
      <h2 class="person-name">MARLOW J. <strong>ASHFORD</strong></h2>
      <p class="person-role">Manager</p>
      <div class="person-rule"></div>
    </div>
    <ul class="contacts">
      <li>
        <span class="contact-icon"><svg viewBox="0 0 12 12"><path d="M6 1a3.5 3.5 0 0 0-3.5 3.5C2.5 7.5 6 11 6 11s3.5-3.5 3.5-6.5A3.5 3.5 0 0 0 6 1z" fill="#fff"/><circle cx="6" cy="4.5" r="1.3" fill="#0f3350"/></svg></span>
        <span>212 Linden Harbor Lane<br>Halden, ME 04011</span>
      </li>
      <li>
        <span class="contact-icon"><svg viewBox="0 0 12 12"><path d="M3 1.5l1.6 2.2-1 1.2a6 6 0 0 0 2.6 2.6l1.2-1 2.2 1.6-.8 1.9C5 9.8 2.2 7 2.1 2.3z" fill="#fff"/></svg></span>
        <span>+1 207 555 0148</span>
      </li>
      <li>
        <span class="contact-icon"><svg viewBox="0 0 12 12"><rect x="1.5" y="3" width="9" height="6" fill="none" stroke="#fff" stroke-width="1.1"/><path d="M1.5 3L6 6.6 10.5 3" fill="none" stroke="#fff" stroke-width="1.1"/></svg></span>
        <span>stay@ashfordhouse.com</span>
      </li>
      <li>
        <span class="contact-icon"><svg viewBox="0 0 12 12"><path d="M3 2l6 4-2.6.6L7.8 9.6 6.7 10.2 5.3 7.2 3.4 9z" fill="#fff"/></svg></span>
        <span>www.ashfordhouse.com</span>
      </li>
    </ul>
    <div class="dot-rule"></div>
    <div class="pattern-band" role="img" aria-label="Soft gold geometric lattice pattern on white"></div>
  </section>

</body>
</html>
```